Marlowen

I'm looking for business cards with the logo I've attached. I don't have an specific idea in mind and open to anything. All the usual info will be involved. Name, position in company, nr, email, address

```html
<!DOCTYPE html>
<html lang="en">
<head>
<meta charset="utf-8">
<title>Marlowen Designs – Business Cards</title>
<link rel="stylesheet" href="https://fonts.googleapis.com/css2?family=Marcellus&family=Public+Sans:wght@400;600&display=swap">
<style>
  :root {
    --backdrop: #8e8e8e;
    --navy: #142947;
    --paper: #d7d7d9;
    --gold: #c9972f;
    --light-text: #d3d6dc;
    --dark-text: #1b2a44;
  }
  * { margin: 0; padding: 0; box-sizing: border-box; }
  html, body { width: 1200px; height: 1101px; overflow: hidden; }
  body {
    background: var(--backdrop);
    position: relative;
    font-family: "Public Sans", Arial, sans-serif;
  }
  .card {
    position: absolute;
    width: 302px;
    height: 529px;
    text-align: center;
  }
  .card--front { left: 246px; top: 269px; background: var(--navy); color: var(--light-text); }
  .card--back { left: 642px; top: 267px; background: var(--paper); color: var(--dark-text); }

  .person { position: absolute; top: 100px; left: 0; right: 0; }
  .person__name {
    font-family: "Marcellus", Georgia, serif;
    font-size: 22px;
    letter-spacing: 0.5px;
    font-weight: 400;
  }
  .person__role {
    font-size: 15px;
    letter-spacing: 4px;
    margin-top: 2px;
  }

  .contact-divider { position: absolute; top: 260px; left: 56px; }

  .contact-list {
    position: absolute; top: 389px; left: 0; right: 0;
    list-style: none;
    font-size: 14.5px;
    line-height: 21.5px;
  }

  .brand-name {
    position: absolute; top: 178px; left: 0; right: 0;
    color: var(--gold);
    font-family: "Public Sans", Arial, sans-serif;
    font-weight: 600;
    font-size: 38px;
    line-height: 46px;
    letter-spacing: 3px;
    text-transform: uppercase;
  }
  .gold-rule {
    position: absolute; top: 345px; left: 117px;
    width: 68px; height: 2px;
    background: linear-gradient(90deg, transparent, var(--gold) 20%, var(--gold) 80%, transparent);
  }
  .address {
    position: absolute; top: 449px; left: 0; right: 0;
    font-style: normal;
    font-size: 14.5px;
    line-height: 21.5px;
  }
</style>
</head>
<body>
  <section class="card card--front">
    <header class="person">
      <h1 class="person__name">ELIAS MORROW</h1>
      <p class="person__role">DIRECTOR</p>
    </header>

    <svg class="contact-divider" width="190" height="30" viewBox="0 0 190 30" aria-hidden="true">
      <defs>
        <linearGradient id="rule-left" x1="0" x2="1"><stop offset="0" stop-color="#c9972f" stop-opacity="0"/><stop offset="1" stop-color="#c9972f"/></linearGradient>
        <linearGradient id="rule-right" x1="0" x2="1"><stop offset="0" stop-color="#c9972f"/><stop offset="1" stop-color="#c9972f" stop-opacity="0"/></linearGradient>
      </defs>
      <rect x="0" y="14" width="52" height="1.6" fill="url(#rule-left)"/>
      <rect x="139" y="14" width="52" height="1.6" fill="url(#rule-right)"/>
      <g fill="none" stroke="#c9972f" stroke-width="1.8">
        <circle cx="68" cy="15" r="11"/>
        <circle cx="96" cy="15" r="11"/>
        <circle cx="124" cy="15" r="11"/>
      </g>
      <path d="M63.5 9.5c1-.8 2-.6 2.5.4l.9 1.8c.3.7 0 1.3-.6 1.7l-.6.4c.6 1.6 1.9 2.9 3.4 3.6l.5-.6c.4-.6 1.1-.8 1.7-.5l1.8.9c1 .5 1.1 1.5.3 2.5-1 1.2-2.6 1.4-4.3.6-2.8-1.3-4.6-3.3-5.8-5.9-.7-1.7-.7-3.6.2-4.9z" fill="#d3d6dc"/>
      <rect x="90.5" y="11" width="11" height="8" rx="1" fill="#d3d6dc"/>
      <path d="M90.8 11.5 96 15.6l5.2-4.1" fill="none" stroke="#142947" stroke-width="1.1"/>
      <g fill="none" stroke="#d3d6dc" stroke-width="1">
        <circle cx="124" cy="15" r="5.8"/>
        <ellipse cx="124" cy="15" rx="2.6" ry="5.8"/>
        <line x1="118.2" y1="15" x2="129.8" y2="15"/>
        <line x1="124" y1="9.2" x2="124" y2="20.8"/>
      </g>
    </svg>

    <ul class="contact-list">
      <li>555.204.3817</li>
      <li>hello@MarlowenDesigns.com</li>
      <li>MarlowenDesigns.com</li>
    </ul>
  </section>

  <section class="card card--back">
    <p class="brand-name">Marlowen<br>Designs</p>
    <div class="gold-rule"></div>
    <address class="address">48 Hartfield Lane,<br>Pine Hollow, WV, 25990</address>
  </section>
</body>
</html>
```